redesign of www.varqolo.com

Need redesign of our website to be more professionally looking. International import & export, warehousing and distribution business primarily from China to North America.

A few professional pictures needed on the new website.

Contact form also is needed.

Total 5 - 10 pages will be OK.

```html
<!DOCTYPE html>
<html lang="en">
<head>
<meta charset="utf-8">
<title>Varqolo — Your Gateway to Asia</title>
<link href="https://fonts.googleapis.com/css2?family=Oswald:wght@400;500&family=Open+Sans:wght@300;400;600&family=Roboto:wght@300;400;500&display=swap" rel="stylesheet">
<style>
:root{
  --orange:#f2a01c;
  --orange-dark:#e07f0c;
  --ink:#2c2c2c;
  --heading:#2f2f2f;
  --nav:#6b6b6b;
  --nav-active:#2e4566;
  --link:#3b5a80;
  --text:#7a7a7a;
  --panel:#eef0f1;
  --page:#eef0f1;
  --footer:#e6e6e6;
  --white:#ffffff;
}
*{margin:0;padding:0;box-sizing:border-box}
html,body{width:1024px;height:1200px;overflow:hidden}
body{position:relative;background:var(--page);font-family:"Roboto",sans-serif;color:var(--text)}
.abs{position:absolute}

/* header */
.header{left:0;top:0;width:1024px;height:83px;background:var(--white);border-top:3px solid var(--ink)}
.inquiry{left:604px;top:0;width:288px;height:26px;background:var(--ink);border-radius:0 0 14px 14px;color:var(--white);font:500 12px "Oswald",sans-serif;display:flex;align-items:center;justify-content:center;gap:7px;letter-spacing:.2px}
.inquiry b{color:var(--orange);font-weight:500}
.brand{left:124px;top:20px;display:flex;align-items:center;gap:8px;font:500 34px "Oswald",sans-serif;color:var(--heading);letter-spacing:1px}
.brand-dot{width:14px;height:14px;border-radius:50%;background:var(--orange)}
.nav-link{top:46px;font:500 12px "Oswald",sans-serif;letter-spacing:.5px;color:var(--nav);text-decoration:none}
.nav-link.active{color:var(--nav-active)}
.contact-btn{left:775px;top:35px;width:112px;height:36px;background:linear-gradient(var(--orange),var(--orange-dark));border-radius:3px;color:var(--white);font:500 12px "Oswald",sans-serif;display:flex;align-items:center;justify-content:center;gap:8px}

/* hero */
.hero{left:0;top:83px;width:1024px;height:398px;background:linear-gradient(180deg,#b9c0c4 0%,#c7a85a 35%,#8a7140 60%,#6d5b3c 100%)}
.hero-arrow{top:236px;width:36px;height:36px;border-radius:50%;display:flex;align-items:center;justify-content:center}
.hero-arrow.prev{left:78px;background:var(--orange)}
.hero-arrow.next{left:904px;background:#3a3a3a}
.hero-title{left:134px;top:306px;font:400 30px "Oswald",sans-serif;color:var(--white);letter-spacing:-.3px}
.hero-text{left:138px;top:355px;width:490px;font:300 13.5px/17.5px "Open Sans",sans-serif;color:var(--white);letter-spacing:-.2px}

/* intro panel */
.panel{left:108px;top:439px;width:803px;height:580px;background:var(--panel);box-shadow:0 0 30px rgba(0,0,0,.12)}
.intro-photo{left:136px;top:478px;width:158px;height:210px;background:linear-gradient(160deg,#dfe7ef,#8da3ba 60%,#2f3e55)}
.h2{font:400 18px "Oswald",sans-serif;color:var(--heading)}
.copy{font:300 9.8px/16px "Roboto",sans-serif;color:var(--text)}
.learn-btn{left:311px;top:659px;width:64px;height:27px;border:1px solid #c9c9c9;border-radius:3px;background:linear-gradient(#fafafa,#e4e4e4);font:400 9px "Open Sans",sans-serif;color:#888;display:flex;align-items:center;justify-content:center}

/* service cards */
.card{top:719px;width:237px;height:271px;background:var(--white);border-top:6px solid var(--orange);box-shadow:0 1px 4px rgba(0,0,0,.15)}
.card h3{margin-top:16px;text-align:center;font:400 16px "Oswald",sans-serif;color:var(--heading)}
.card .media{margin:10px 18px 0;height:105px}
.card p{margin:20px 20px 0;font:400 10.5px/15px "Open Sans",sans-serif;color:#666}
.card a{display:block;margin:15px 20px 0;font:600 11px "Open Sans",sans-serif;color:var(--link)}

/* footer */
.footer{left:0;top:1018px;width:1024px;height:146px;background:var(--footer);border-top:1px solid #dcdcdc}
.f-brand{left:132px;top:1068px;display:flex;align-items:center;gap:6px;font:500 24px "Oswald",sans-serif;color:var(--heading);letter-spacing:1px}
.f-brand .brand-dot{width:10px;height:10px}
.f-col h4{font:600 12px "Open Sans",sans-serif;color:#666;margin-bottom:10px}
.f-col li{list-style:none;font:400 8.5px/19px "Open Sans",sans-serif;color:#888;padding-left:10px;position:relative}
.f-col li::before{content:"";position:absolute;left:0;top:7px;border:3px solid transparent;border-left:3.5px solid #999}
.f-col li.hover{color:var(--orange)}
.contact-row{display:flex;gap:10px;font:400 8.5px/24px "Open Sans",sans-serif;color:#888}
.contact-row svg{margin-top:7px;flex:none}
.social{display:flex;gap:7px}
.social span{width:29px;height:29px;border-radius:3px;background:#6e7e8e}
.bottom{left:0;top:1164px;width:1024px;height:36px;background:var(--orange);font:400 8.5px "Roboto",sans-serif;color:#5b3a06}
</style>
</head>
<body>

<header class="abs header"></header>
<div class="abs inquiry">
  <svg width="14" height="14" viewBox="0 0 14 14"><circle cx="7" cy="7" r="6" fill="none" stroke="#fff" stroke-width="1.2"/><path d="M5 4.2l1 1.6-.6.8c.4.9 1 1.5 1.9 1.9l.8-.6 1.6 1-.5 1c-2.4-.2-4.4-2.2-4.6-4.6z" fill="#fff"/></svg>
  FOR INQUIRIES, CALL US: <b>1-800-555-01962</b>
</div>
<div class="abs brand"><span class="brand-dot"></span>VARQOLO</div>
<nav>
  <a class="abs nav-link active" href="#" style="left:494px">HOME</a>
  <a class="abs nav-link" href="#" style="left:552px">ABOUT US</a>
  <a class="abs nav-link" href="#" style="left:631px">SERVICES</a>
  <a class="abs nav-link" href="#" style="left:708px">SERVICES</a>
</nav>
<div class="abs contact-btn">
  <svg width="18" height="13" viewBox="0 0 18 13"><rect x="1" y="1" width="16" height="11" rx="1" fill="none" stroke="#fff" stroke-width="1.4"/><path d="M1.5 1.5l7.5 6 7.5-6" fill="none" stroke="#fff" stroke-width="1.4"/></svg>
  CONTACT US
</div>

<section class="abs hero" role="img" aria-label="Red truck crossing a long bridge past autumn forest and a lake"></section>
<div class="abs hero-arrow prev"><svg width="8" height="10" viewBox="0 0 8 10"><path d="M6 1L2 5l4 4" fill="none" stroke="#fff" stroke-width="1.6"/></svg></div>
<div class="abs hero-arrow next"><svg width="8" height="10" viewBox="0 0 8 10"><path d="M2 1l4 4-4 4" fill="none" stroke="#fff" stroke-width="1.6"/></svg></div>
<h1 class="abs hero-title">Your Gateway to Asia</h1>
<p class="abs hero-text">We are committed to utilize the MOST COST EFFECTIVE resources to help our clients in product development, prototyping, sampling, manufacturing, arranging custom clearance &amp; shipment delivery to the door in a hassle free environment.</p>

<section class="abs panel"></section>
<div class="abs intro-photo" role="img" aria-label="Business handshake between two people in suits"></div>
<h2 class="abs h2" style="left:311px;top:468px">Welcome to Varqolo Inc.</h2>
<p class="abs copy" style="left:313px;top:504px;width:295px">It is a long established fact that a reader will be distracted by the readable content of a page when looking at its layout. The point of using Lorem Ipsum is that it has a more-or-less normal distri-bution of letters, as opposed to using 'Content here, content here', making it look like readable English.</p>
<p class="abs copy" style="left:313px;top:600px;width:295px">Lorem ipsum dolor sit amet, consectetur adipisicing elit, sed do eiusmod tempor incididunt ut labore et dolore magna aliqua. Ut enim ad minim veniam, quis nostrud exercitation ullamco laboris</p>
<div class="abs learn-btn">Learn More</div>

<h2 class="abs h2" style="left:649px;top:468px">Varqolo Goal</h2>
<p class="abs copy" style="left:647px;top:504px;width:240px">It is a long established fact that a reader will be distracted by the readable content of a page when looking at its layout. The point of using Lorem Ipsum is that it has a more-or-less normal distribution</p>
<h2 class="abs h2" style="left:649px;top:588px">Varqolo Principle</h2>
<p class="abs copy" style="left:647px;top:624px;width:240px">It is a long established fact that a reader will be distracted by the readable content of a page when looking at its layout. The point of using Lorem Ipsum is that it has a more-or-less normal distribution</p>

<article class="abs card" style="left:133px">
  <h3>IMPORT &amp; EXPORT</h3>
  <div class="media" role="img" aria-label="Container ship loaded with cargo at sea" style="background:linear-gradient(180deg,#c9dcec 0%,#9fbfd8 45%,#2f3a4a 70%,#4c79a6 100%)"></div>
  <p>Lorem ipsum dolor sit amet, consectetur adipisicing elit, sed do eiusmod tempor incididunt ut labore .</p>
  <a href="#">READ MORE</a>
</article>
<article class="abs card" style="left:390px">
  <h3>WAREHOUSING &amp; DISTRIBUTION</h3>
  <div class="media" role="img" aria-label="Forklift in a warehouse with stacked cardboard boxes" style="background:linear-gradient(180deg,#8a6a3e 0%,#c39a62 45%,#9aa4b0 75%,#e6e6e6 100%)"></div>
  <p>Lorem ipsum dolor sit amet, consectetur adipisicing elit, sed do eiusmod tempor incididunt ut labore .</p>
  <a href="#">READ MORE</a>
</article>
<article class="abs card" style="left:647px">
  <h3>SOURCING</h3>
  <div class="media" role="img" aria-label="Business team reviewing documents at a table" style="background:linear-gradient(120deg,#c98a6a 0%,#e8e2dc 45%,#f4f4f4 70%,#cfd6dc 100%)"></div>
  <p>Lorem ipsum dolor sit amet, consectetur adipisicing elit, sed do eiusmod tempor incididunt ut labore .</p>
  <a href="#">READ MORE</a>
</article>

<footer class="abs footer"></footer>
<div class="abs f-brand"><span class="brand-dot"></span>VARQOLO</div>
<div class="abs f-col" style="left:321px;top:1042px">
  <h4>Navigation</h4>
  <ul><li>Home</li><li>About</li><li>Services</li><li>Contact</li></ul>
</div>
<div class="abs f-col" style="left:448px;top:1042px">
  <h4>Services</h4>
  <ul><li class="hover">Service</li><li>Service</li><li>Service</li><li>Service</li></ul>
</div>
<div class="abs f-col" style="left:577px;top:1042px">
  <h4>Contact Us</h4>
  <div class="contact-row"><svg width="10" height="10" viewBox="0 0 10 10"><path d="M2 0.5l2 2.5-1 1.3c.6 1.3 1.4 2.1 2.7 2.7L7 6l2.5 2-1 1.5C4.6 9.3.7 5.4.5 1.5z" fill="#999"/></svg>+1800-555-0196</div>
  <div class="contact-row"><svg width="10" height="8" viewBox="0 0 10 8"><rect width="10" height="8" fill="#999"/><path d="M0 0l5 4 5-4" fill="none" stroke="#e6e6e6" stroke-width="1"/></svg>info@yourwebsite.com</div>
  <div class="contact-row"><svg width="10" height="12" viewBox="0 0 10 12"><path d="M5 0a4 4 0 0 1 4 4c0 3-4 8-4 8S1 7 1 4a4 4 0 0 1 4-4z" fill="#999"/><circle cx="5" cy="4" r="1.5" fill="#e6e6e6"/></svg><span>Your Address, Your Country<br>Your Zip Code</span></div>
</div>
<div class="abs f-col" style="left:750px;top:1042px">
  <h4>Social</h4>
  <div class="social"><span aria-label="Social link"></span><span aria-label="Social link"></span><span aria-label="Social link"></span><span aria-label="Social link"></span></div>
</div>

<div class="abs bottom">
  <span class="abs" style="left:134px;top:12px">Copyright 2014 © Varqolo - All Rights Reserved</span>
  <span class="abs" style="left:778px;top:12px">Site Map &nbsp;&nbsp;•&nbsp;&nbsp; Privacy Policy</span>
</div>

</body>
</html>
```